Chiro Card
Bright Path Chiropractic & Wellness
Project: Chiro Card
Chiro Card -
Creative Brief
Simple
Marcus Hale
Chiropractor
812 Orvale Ave, Suite K Corbin Falls, Tx. 78245
corbinfallsspine@mailvane.com
www.corbinfallsspine.com
Please do not include my email address on the business card.

```html
<!DOCTYPE html>
<html lang="en">
<head>
<meta charset="utf-8">
<title>Bright Path Chiropractic &amp; Wellness – Stationery Set</title>
<link href="https://fonts.googleapis.com/css2?family=Cinzel:wght@700&family=Open+Sans:wght@400;600&display=swap" rel="stylesheet">
<style>
  :root{
    --bg-center:#4a4a4a;
    --bg-edge:#262626;
    --paper:#ffffff;
    --paper-shade:#eef0f2;
    --green:#5c9e3a;
    --green-light:#8cc063;
    --blue:#1b5f9c;
    --blue-dark:#103f6e;
    --ink:#4d4d4d;
    --ink-light:#9a9a9a;
  }
  *{box-sizing:border-box;margin:0;padding:0}
  html,body{width:1200px;height:346px;overflow:hidden}
  body{
    position:relative;
    background:radial-gradient(ellipse at 50% 45%,var(--bg-center),var(--bg-edge) 80%);
    font-family:"Open Sans",Arial,sans-serif;
    color:var(--ink);
  }
  .piece{position:absolute;background:var(--paper);box-shadow:0 3px 8px rgba(0,0,0,.5)}
  .brand{font-family:"Cinzel",Georgia,serif;font-weight:700;color:var(--green);line-height:1.05;display:flex;align-items:center;gap:4px}
  .brand-dot{display:inline-block;border-radius:50%;background:var(--green);flex:none}

  /* standalone logo */
  .logo-lockup{position:absolute;left:12px;top:26px;width:100px;font-size:13px}
  .logo-lockup .brand-dot{width:12px;height:12px}

  /* business cards */
  .card{left:19px;width:96px;height:74px;overflow:hidden}
  .card-front{top:108px}
  .card-back{top:206px}
  .card .brand{font-size:7px;padding:8px 6px 0}
  .card .brand-dot{width:6px;height:6px}
  .card-band{position:absolute;left:0;right:0;bottom:0;background:linear-gradient(var(--blue),var(--blue-dark));border-top:2px solid var(--green-light);color:#fff;font-size:3.2px;line-height:1.4;padding:3px 6px}
  .card-front .card-band{height:28px}
  .card-back .card-band{height:40px}
  .card-band .name{font-weight:600;font-size:4px}

  /* letterheads */
  .letterhead{top:10px;width:216px;height:302px}
  .letterhead-a{left:168px}
  .letterhead-b{left:403px}
  .letterhead .brand{position:absolute;left:14px;top:14px;font-size:9px;width:90px}
  .letterhead .brand-dot{width:8px;height:8px}
  .letterhead .addr{position:absolute;right:14px;top:16px;width:70px;font-size:3.5px;color:var(--ink-light);line-height:1.4}
  .letterhead .watermark{position:absolute;left:50%;top:42%;width:70px;height:70px;margin:-35px 0 0 -35px;border-radius:50%;background:var(--paper-shade)}
  .letterhead-foot{position:absolute;left:0;right:0;bottom:0;height:14px;background:linear-gradient(var(--blue),var(--blue-dark));border-top:2px solid var(--green-light);color:#fff;font-size:3.3px;text-align:center;line-height:12px}

  /* envelope fronts */
  .env-front{left:643px;width:185px;height:103px;overflow:hidden}
  .env-front-a{top:72px}
  .env-front-b{top:199px}
  .env-front .brand{position:absolute;left:10px;top:10px;font-size:9px;width:90px}
  .env-front .brand-dot{width:8px;height:8px}
  .env-front .watermark{position:absolute;right:30px;top:18px;width:56px;height:56px;border-radius:50%;background:var(--paper-shade)}
  .env-front .env-foot{position:absolute;left:0;right:0;bottom:0;height:10px;background:linear-gradient(var(--blue),var(--blue-dark));border-top:2px solid var(--green-light)}
  .env-front .return{position:absolute;left:10px;bottom:14px;font-size:3.3px;color:var(--ink-light)}

  /* envelope backs */
  .env-back{left:835px;width:353px;height:96px;background:transparent;box-shadow:none}
  .env-back svg{display:block;filter:drop-shadow(0 3px 5px rgba(0,0,0,.5))}
  .env-back-green{top:48px}
  .env-back-blue{top:140px}
  .env-back-white{top:224px}
  .env-back .web{position:absolute;left:0;right:0;top:66px;text-align:center;font-size:3.5px;color:#fff}
  .env-back-white .web{color:var(--ink-light)}
</style>
</head>
<body>

  <div class="logo-lockup brand"><span class="brand-dot"></span><span>Bright Path Chiropractic &amp; Wellness</span></div>

  <div class="piece card card-front">
    <div class="brand"><span class="brand-dot"></span><span>Bright Path Chiropractic &amp; Wellness</span></div>
    <div class="card-band">
      <div class="name">Marcus Hale</div>
      <div>Chiropractor</div>
      <div>www.corbinfallsspine.com</div>
    </div>
  </div>

  <div class="piece card card-back">
    <div class="brand"><span class="brand-dot"></span><span>Bright Path Chiropractic &amp; Wellness</span></div>
    <div class="card-band">
      <div class="name">Marcus Hale</div>
      <div>Chiropractor</div>
      <div>812 Orvale Ave, Suite K</div>
      <div>Corbin Falls, Tx. 78245</div>
      <div>www.corbinfallsspine.com</div>
    </div>
  </div>

  <div class="piece letterhead letterhead-a">
    <div class="brand"><span class="brand-dot"></span><span>Bright Path Chiropractic &amp; Wellness</span></div>
    <div class="addr">812 Orvale Ave, Suite K<br>Corbin Falls, Tx. 78245<br>www.corbinfallsspine.com</div>
    <div class="watermark"></div>
    <div class="letterhead-foot">812 Orvale Ave, Suite K Corbin Falls, Tx. 78245 &nbsp;|&nbsp; corbinfallsspine@mailvane.com &nbsp;|&nbsp; www.corbinfallsspine.com</div>
  </div>

  <div class="piece letterhead letterhead-b">
    <div class="brand"><span class="brand-dot"></span><span>Bright Path Chiropractic &amp; Wellness</span></div>
    <div class="addr">812 Orvale Ave, Suite K<br>Corbin Falls, Tx. 78245<br>www.corbinfallsspine.com</div>
    <div class="watermark"></div>
    <div class="letterhead-foot">812 Orvale Ave, Suite K Corbin Falls, Tx. 78245 &nbsp;|&nbsp; corbinfallsspine@mailvane.com &nbsp;|&nbsp; www.corbinfallsspine.com</div>
  </div>

  <div class="piece env-front env-front-a">
    <div class="brand"><span class="brand-dot"></span><span>Bright Path Chiropractic &amp; Wellness</span></div>
    <div class="watermark"></div>
    <div class="return">www.corbinfallsspine.com</div>
    <div class="env-foot"></div>
  </div>

  <div class="piece env-front env-front-b">
    <div class="brand"><span class="brand-dot"></span><span>Bright Path Chiropractic &amp; Wellness</span></div>
    <div class="watermark"></div>
    <div class="return">www.corbinfallsspine.com</div>
    <div class="env-foot"></div>
  </div>

  <div class="piece env-back env-back-green">
    <svg width="353" height="96" viewBox="0 0 353 96">
      <rect width="353" height="96" fill="#fff"/>
      <path d="M0 0 H353 L176 78 Z" fill="var(--green)"/>
      <path d="M0 96 L176 40 L353 96" fill="none" stroke="#e2e4e6"/>
    </svg>
    <div class="web">www.corbinfallsspine.com</div>
  </div>

  <div class="piece env-back env-back-blue">
    <svg width="353" height="96" viewBox="0 0 353 96">
      <rect width="353" height="96" fill="#fff"/>
      <path d="M0 0 H353 L176 78 Z" fill="var(--blue)"/>
      <path d="M0 96 L176 40 L353 96" fill="none" stroke="#e2e4e6"/>
    </svg>
    <div class="web">www.corbinfallsspine.com</div>
  </div>

  <div class="piece env-back env-back-white">
    <svg width="353" height="96" viewBox="0 0 353 96">
      <rect width="353" height="96" fill="#fff"/>
      <path d="M0 0 L176 60 L353 0" fill="none" stroke="#d6d8da"/>
      <path d="M0 96 L176 40 L353 96" fill="none" stroke="#e2e4e6"/>
    </svg>
  </div>

</body>
</html>
```